Restaurant menu design

I need a menu for a restaurant in Spain.
It has to be bohemian but modern. We need something romantic and elegant.
The restaurant is elegant with good food and an excellent reputation. It is also modern at the same time.
The restaurant is superbly decorated and very chick so we need something "class" to fit in with the surroundings.
The size of the document must be 325 mm in high and 245 mm as a maximum and preferably made in indesign.

Reason: Thank you all for your designs.
So far all your designs are ok but it isn´t what we are looking for. Most of the designs are too loaded, too many colors and too much decoration.

Target Market(s)

Adults of various age groups and different nationalities mostly European.

Industry/Entity Type

Restaurant

Requirements
Must have
• The menu must have two interior pages with the text as in the document attached.It must be easily legible.
Nice to have
• See what kind of menus they use in important restaurants in places like Paris, see what designs are in trend, but Not necessarily doing the same style if it doesn’t fit in with the description above.
Should not have
• Nothing old fashioned.

```html
<!DOCTYPE html>
<html lang="es">
<head>
<meta charset="utf-8">
<title>La Violette — Carta</title>
<link rel="stylesheet" href="https://fonts.googleapis.com/css2?family=Parisienne&family=Cormorant+Garamond:ital,wght@0,400;1,400&display=swap">
<style>
  :root {
    --plum: #98356f;
    --plum-soft: #b0528a;
    --rose: #c77aa8;
    --rose-pale: #e9c6da;
    --ink: #5a3a4c;
    --paper: #ffffff;
    --canvas: #ffffff;
    --shade: rgba(0,0,0,0.12);
  }
  * { margin: 0; padding: 0; box-sizing: border-box; }
  html, body { width: 872px; height: 1200px; overflow: hidden; background: var(--canvas); }
  .sheet { position: relative; width: 872px; height: 1200px; }

  /* Cover spread */
  .cover { position: absolute; left: 0; top: 0; width: 872px; height: 372px; }
  .cover-back { position: absolute; left: 0; top: 0; width: 436px; height: 372px; background: var(--paper); box-shadow: 0 0 4px var(--shade); }
  .cover-front { position: absolute; left: 436px; top: 0; width: 436px; height: 372px; background: var(--plum); overflow: hidden; }
  .brand-box { position: absolute; left: 226px; top: 20px; width: 130px; height: 130px; background: var(--paper); display: flex; flex-direction: column; align-items: center; justify-content: center; gap: 8px; }
  .brand-name { font-family: "Cormorant Garamond", serif; font-size: 22px; color: var(--plum); letter-spacing: 0.5px; }
  .brand-dot { width: 10px; height: 10px; border-radius: 50%; background: var(--plum); }
  .cover-watermark { position: absolute; font-family: "Cormorant Garamond", serif; color: rgba(255,255,255,0.28); line-height: 1; }
  .cover-watermark.one { left: 94px; top: 226px; font-size: 92px; }
  .cover-watermark.two { left: 0px; top: 300px; font-size: 120px; }

  /* Interior spread */
  .page { position: absolute; top: 380px; width: 436px; height: 820px; background: var(--paper); box-shadow: 0 0 5px var(--shade); }
  .page.left { left: 0; }
  .page.right { left: 436px; }

  .section { position: absolute; left: 0; width: 436px; text-align: center; }
  .section-title { display: flex; align-items: center; justify-content: center; gap: 12px; font-family: "Parisienne", cursive; font-size: 20px; color: var(--rose); height: 26px; }
  .section-title::before, .section-title::after { content: ""; width: 60px; height: 1px; background: var(--rose-pale); }
  .dish { font-family: "Cormorant Garamond", serif; font-style: italic; font-size: 10px; color: var(--ink); line-height: 15px; }
  .dish .price { margin-left: 6px; }
  .rule { width: 250px; margin: 8px auto 0; border-top: 1px dashed var(--rose-pale); }

  .sauce-band { position: absolute; left: 20px; top: 256px; width: 404px; height: 16px; background: var(--rose); color: #fff; font-family: "Cormorant Garamond", serif; font-style: italic; font-size: 9px; line-height: 16px; text-align: center; }

  .figure-mark { position: absolute; left: 4px; top: 650px; width: 30px; height: 60px; background: linear-gradient(180deg, var(--plum-soft), var(--plum)); border-radius: 14px 14px 4px 4px; opacity: 0.8; }
</style>
</head>
<body>
<div class="sheet">

  <section class="cover">
    <div class="cover-back"></div>
    <div class="cover-front">
      <div class="brand-box">
        <span class="brand-name">la violette</span>
        <span class="brand-dot"></span>
      </div>
      <div class="cover-watermark one">la</div>
      <div class="cover-watermark two">violette</div>
    </div>
  </section>

  <article class="page left">
    <div class="section" style="top:44px">
      <h2 class="section-title">Entrantes</h2>
      <p class="dish">Ensalada La Violette Lechuga, tomate <span class="price">15,50€</span></p>
      <p class="dish">Ensalada Caprese (Tomate y Mozzarella) <span class="price">13,5€</span></p>
      <p class="dish">Ensalada de Queso de Cabra con Nueces <span class="price">14,5€</span></p>
      <p class="dish">Cóctel de Gambas, Langostinos y Aguacate <span class="price">16,0€</span></p>
      <p class="dish">La Sopa de Cebolla <span class="price">9,5€</span></p>
      <p class="dish">Crema de Espárragos Trigueros y Almendras <span class="price">10,0€</span></p>
      <p class="dish">Carpaccio de Ternera <span class="price">15,5€</span></p>
      <p class="dish">Carpaccio de Salmón Ahumado y Eneldo <span class="price">14,5€</span></p>
      <p class="dish">Carpaccio de Atún <span class="price">16,0€</span></p>
      <p class="dish">Mejillones en Salsa de Vino Blanco <span class="price">12,5€</span></p>
      <p class="dish">Parrillada de Verduras <span class="price">11,0€</span></p>
      <p class="dish">Parrillada de Verduras Gratinada al Queso de Cabra <span class="price">13,0€</span></p>
      <p class="dish">Tostas Royal de la Casa <span class="price">12,0€</span></p>
      <div class="rule"></div>
    </div>

    <div class="section" style="top:296px">
      <h2 class="section-title">Pescados al Grill</h2>
      <p class="dish">Salmón al Horno <span class="price">17,5€</span></p>
      <p class="dish">Lubina Plancha con Salsa Verde y Almejas <span class="price">19,0€</span></p>
      <p class="dish">Filete de Dorada a la Sal de Mar <span class="price">18,5€</span></p>
      <p class="dish">Dorada al Horno con Patatas <span class="price">17,0€</span></p>
      <p class="dish">Langostinos al Grill con Ajo y Perejil <span class="price">21,0€</span></p>
      <p class="dish">Pescado del Día a la Brasa <span class="price">19,5€</span></p>
      <p class="dish">Lomo de Bacalao con Pisto Casero <span class="price">18,0€</span></p>
      <p class="dish">Parrillada de Pescado y Marisco <span class="price">24,0€</span></p>
      <div class="rule"></div>
    </div>

    <div class="section" style="top:488px">
      <h2 class="section-title">Especial Pasta</h2>
      <p class="dish">Tallarines Frutti di Mare al Cartoccio <span class="price">14,5€</span></p>
      <p class="dish">Raviolis Rellenos de Trufa <span class="price">15,0€</span></p>
      <div class="rule"></div>
    </div>

    <div class="figure-mark" role="img" aria-label="Small illustrated figure in plum tones"></div>
  </article>

  <article class="page right">
    <div class="section" style="top:44px">
      <h2 class="section-title">Carnes</h2>
      <p class="dish">Pechuga de Pollo con Salsa de Champiñones y Nata <span class="price">14,0€</span></p>
      <p class="dish">Chuleta de Cordero <span class="price">19,5€</span></p>
      <p class="dish">Solomillo de Cerdo con Salsa Pimienta <span class="price">16,0€</span></p>
      <p class="dish">Solomillo de Ternera a la Plancha <span class="price">22,0€</span></p>
      <p class="dish">Entrecot de Ternera con Patatas Panaderas <span class="price">20,0€</span></p>
      <p class="dish">Solomillo de Ternera con Foie y Reducción de Oporto <span class="price">24,5€</span></p>
      <p class="dish">Hamburguesa de Ternera con Queso Brie y Cebolla Caramelizada <span class="price">15,5€</span></p>
      <p class="dish">Brocheta de Ternera <span class="price">17,0€</span></p>
      <p class="dish">T-bone Steak de Ternera <span class="price">26,0€</span></p>
      <p class="dish">Chuletón de Ternera <span class="price">28,0€</span></p>
      <p class="dish">Parrillada de Carnes a Elección <span class="price">23,5€</span></p>
    </div>
    <div class="sauce-band">Salsas: Pimienta · Roquefort · Setas · Mostaza · Miel · Verde</div>

    <div class="section" style="top:292px">
      <h2 class="section-title">Los Postres de la Violette</h2>
      <p class="dish">Profiteroles "La Violette" <span class="price">6,5€</span></p>
      <p class="dish">Coulant de Chocolate Negro <span class="price">6,5€</span></p>
      <p class="dish">Sorbete de Limón, Frutas de Pasión o Mango <span class="price">5,5€</span></p>
      <p class="dish">Pastel de Chocolate Caliente con Helado de Vainilla <span class="price">6,5€</span></p>
      <p class="dish">Crème Brûlée <span class="price">6,0€</span></p>
      <p class="dish">Tarta de Manzana Casera "Tatin" y Helado de Canela <span class="price">6,5€</span></p>
      <p class="dish">Copa Helado Mixto <span class="price">5,5€</span></p>
      <p class="dish">Fondue de Chocolate con Fruta de Temporada <span class="price">12,0€</span></p>
      <p class="dish">Tarta de Queso con Coulis de Frutos Rojos <span class="price">6,0€</span></p>
      <p class="dish">Mousse Blanca de Chocolate <span class="price">5,5€</span></p>
      <div class="rule"></div>
    </div>
  </article>

</div>
</body>
</html>
```